Website to help teachers create worksheets and tests for their students

I'm after a completely designed website that is easy to use for older parents and teachers to generate worksheets. There are attached screenshots of what the current basic user interface is like along with a sample generated HTML and PDF worksheet. The uploaded page is currently all there is to the website, however I'd also like a home page to be designed with screen elements allowing users to login and sign up.

Target Market(s)

Parents and Teachers of children learning English and Mathematics less than the age of 14.

```html
<!DOCTYPE html>
<html lang="en">
<head>
<meta charset="utf-8">
<title>Sheetwright – Math Worksheets</title>
<link href="https://fonts.googleapis.com/css2?family=Fira+Sans:wght@400;500;600&family=Oxygen:wght@400;700&display=swap" rel="stylesheet">
<style>
:root{
  --orange:#f29a2e;
  --orange-panel:#f6a623;
  --green:#8dc026;
  --green-text:#3a9a2a;
  --blue:#338ee0;
  --blue-dark:#1479bd;
  --teal:#0f9ec9;
  --cyan-btn:#0b9ac8;
  --text:#3a3a3a;
  --muted:#8a8a8a;
  --caption:#c0620a;
  --line:#cfcfcf;
  --footer:#3d8fd6;
  --red:#d9342b;
}
*{box-sizing:border-box;margin:0;padding:0}
html,body{width:1050px;height:1200px;overflow:hidden;background:#fff}
body{position:relative;font-family:"Oxygen",sans-serif;color:var(--text)}
.abs{position:absolute}

/* header */
.account-bar{left:726px;top:3px;font-size:10px;color:var(--muted);font-weight:700}
.account-bar a{color:var(--orange);text-decoration:none;margin-left:4px}
.account-bar svg{vertical-align:middle;margin-left:3px}
.brand{left:140px;top:33px;font-family:"Fira Sans",sans-serif;font-weight:600;font-size:26px;color:var(--orange);letter-spacing:.3px}
.main-nav{left:462px;top:44px;display:flex;gap:19px;font-size:12.5px;font-weight:700;color:#8b8b8b}
.signup{left:861px;top:37px;width:74px;height:27px;background:var(--cyan-btn);color:#fff;border-radius:3px;font-size:12px;font-weight:700;display:flex;align-items:center;justify-content:center;letter-spacing:.3px}

/* hero */
.hero{left:0;top:95px;width:1050px;height:166px;background:linear-gradient(90deg,#4d7f95 0%,#3f7286 45%,#2d5a6d 75%,#26495a 100%)}
.hero-shade{left:0;top:95px;width:1050px;height:166px;background:rgba(20,70,90,.35)}
.hero-title{left:0;top:114px;width:1044px;text-align:center;font-family:"Fira Sans",sans-serif;font-weight:600;font-size:29px;color:#fff}
.hero-rule{left:437px;top:167px;width:175px;height:1px;background:rgba(255,255,255,.8)}
.hero-text{left:0;top:178px;width:1050px;text-align:center;font-family:"Fira Sans",sans-serif;font-size:19px;line-height:32px;color:#fff}

/* problem type bar */
.type-bar{left:0;top:261px;width:1050px;height:34px;background:var(--blue)}
.type-item{top:261px;height:34px;display:flex;align-items:center;font-size:11.5px;color:#fff;gap:9px}
.type-item.active{background:var(--blue-dark);padding:0 9px}

.tagline{left:0;top:322px;width:1070px;text-align:center;font-size:13.5px;font-weight:700;color:var(--green-text)}

/* sidebar */
.topic-list{left:140px;top:372px;width:152px;list-style:none}
.topic-list li{height:33.25px;display:flex;align-items:center;justify-content:space-between;font-size:10.5px;font-weight:700;color:#444}

/* panels */
.panel{border:2px solid;background:#fff}
.panel-head{height:37px;display:flex;align-items:center;padding-left:11px;font-family:"Fira Sans",sans-serif;font-weight:500;font-size:15px;color:#fff}
.options{left:306px;top:363px;width:337px;height:608px;border-color:var(--green)}
.options .panel-head{background:var(--green)}
.generator{left:652px;top:363px;width:302px;height:608px;border-color:var(--orange-panel)}
.generator .panel-head{background:var(--orange-panel);padding-left:27px}

.dropdown{height:25px;border:1px solid #c9c9c9;display:flex;align-items:center;justify-content:space-between;padding:0 6px;font-size:10px;color:#a0a0a0;background:#fff}

.flashcard{border-collapse:collapse}
.flashcard td{width:35.5px;height:24.5px;border:1px solid var(--line);text-align:center;font-size:10.5px;font-weight:700;color:var(--teal)}
.flashcard.plain td{border:none;height:25px}
.thumb{border-radius:4px}
.caption{font-size:10.5px;color:var(--caption);text-align:center}

/* generator form */
.field-label{font-size:10.5px;color:#333;text-align:right;width:120px;line-height:16px}
.select{width:130px;height:23px;border:1px solid #c9c9c9;display:flex;font-size:9px;color:#a8a8a8}
.select span{flex:1;padding-left:5px;display:flex;align-items:center}
.select i{width:22px;border-left:1px solid #c9c9c9;display:flex;align-items:center;justify-content:center}
.radio{display:flex;align-items:center;gap:6px;font-size:10.5px;color:#333}
.radio b{width:12px;height:12px;border:1.5px solid var(--teal);border-radius:50%;display:flex;align-items:center;justify-content:center}
.radio b::after{content:"";width:6px;height:6px;border-radius:50%;background:var(--teal);display:none}
.radio.on b::after{display:block}
.format-icon{width:24px;height:28px;border-radius:2px}
.generate{left:752px;top:913px;width:118px;height:34px;border:2px solid var(--red);display:flex;align-items:center;justify-content:center;font-family:"Fira Sans",sans-serif;font-size:15px;font-weight:500;letter-spacing:.5px;color:#333}

/* footer */
.footer{left:0;top:1112px;width:1050px;height:88px;background:var(--footer);border-top:2px solid #6aa9e2}
.foot-links{display:flex;font-size:9.5px;color:#fff;align-items:center}
.foot-links span.sep{margin:0 8px;opacity:.6}
.foot-rule{left:130px;top:1154px;width:411px;height:1px;background:rgba(255,255,255,.35)}
.foot-head{font-size:10px;color:#fff}
.newsletter{left:590px;top:1153px;width:164px;height:27px;background:#2a6fae;border:1px solid #6aa9e2;border-radius:2px;display:flex;align-items:center;justify-content:space-between;padding:0 2px 0 6px;font-size:9px;color:#d8e9f8}
.newsletter b{background:#1467b4;color:#fff;font-weight:400;font-size:9px;padding:4px 6px;border-radius:2px;border:1px solid #4a9be0}
.social{width:20px;height:20px}
</style>
</head>
<body>

<!-- header -->
<div class="abs account-bar">Already have an account?<a>Sign in here</a><svg width="8" height="5"><path d="M0 0h8L4 5z" fill="#f29a2e"/></svg></div>
<div class="abs brand">Sheetwright</div>
<nav class="abs main-nav"><span>About us</span><span>Community</span><span>How it Works</span><span>Blog</span><span>Contact Us</span></nav>
<div class="abs signup">SIGN UP</div>

<!-- hero -->
<div class="abs hero" role="img" aria-label="Photo of a young girl working at a laptop at home"></div>
<div class="abs hero-shade"></div>
<h1 class="abs hero-title">Dynamically Created Math Worksheets</h1>
<div class="abs hero-rule"></div>
<p class="abs hero-text">Sheetwright is a free, easy to use online tool that helps parents and teachers<br>create worksheets for students to practice their skills at home and in class</p>

<!-- problem type bar -->
<div class="abs type-bar"></div>
<div class="abs type-item" style="left:141px">Problem Type
  <svg width="11" height="9" style="margin-left:12px"><path d="M0 1h11M0 4.5h11M0 8h11" stroke="#fff" stroke-width="1.6"/></svg></div>
<div class="abs type-item active" style="left:254px;width:113px">Number Problem
  <svg width="8" height="5"><path d="M0 0h8L4 5z" fill="#fff"/></svg></div>
<div class="abs type-item" style="left:387px">Word Problem
  <svg width="8" height="5" style="margin-left:4px"><path d="M0 0h8L4 5z" fill="#fff"/></svg></div>

<p class="abs tagline">Generate free printable math worksheets for addition, subtraction, multiplication and pre algebra.</p>

<!-- sidebar -->
<ul class="abs topic-list">
  <li>Counting<svg width="4" height="7"><path d="M0 0l4 3.5L0 7z" fill="#555"/></svg></li>
  <li>Addition Addition<svg width="4" height="7"><path d="M0 0l4 3.5L0 7z" fill="#555"/></svg></li>
  <li>Subtraction Subtraction<svg width="4" height="7"><path d="M0 0l4 3.5L0 7z" fill="#555"/></svg></li>
  <li>Multiplication<svg width="4" height="7"><path d="M0 0l4 3.5L0 7z" fill="#555"/></svg></li>
  <li>Division<svg width="4" height="7"><path d="M0 0l4 3.5L0 7z" fill="#555"/></svg></li>
  <li>Arithmetic Operations<svg width="4" height="7"><path d="M0 0l4 3.5L0 7z" fill="#555"/></svg></li>
  <li>Place Value<svg width="4" height="7"><path d="M0 0l4 3.5L0 7z" fill="#555"/></svg></li>
  <li>Ordinal Numbers<svg width="4" height="7"><path d="M0 0l4 3.5L0 7z" fill="#555"/></svg></li>
  <li>Fractions<svg width="4" height="7"><path d="M0 0l4 3.5L0 7z" fill="#555"/></svg></li>
  <li>Exponents<svg width="4" height="7"><path d="M0 0l4 3.5L0 7z" fill="#555"/></svg></li>
  <li>Rounding<svg width="4" height="7"><path d="M0 0l4 3.5L0 7z" fill="#555"/></svg></li>
  <li>Decimals<svg width="4" height="7"><path d="M0 0l4 3.5L0 7z" fill="#555"/></svg></li>
  <li>Factors<svg width="4" height="7"><path d="M0 0l4 3.5L0 7z" fill="#555"/></svg></li>
  <li>Prime Numbers<svg width="4" height="7"><path d="M0 0l4 3.5L0 7z" fill="#555"/></svg></li>
  <li>Percentage Percentage<svg width="4" height="7"><path d="M0 0l4 3.5L0 7z" fill="#555"/></svg></li>
  <li>Ratio Ratio<svg width="4" height="7"><path d="M0 0l4 3.5L0 7z" fill="#555"/></svg></li>
  <li>Order of Operations<svg width="4" height="7"><path d="M0 0l4 3.5L0 7z" fill="#555"/></svg></li>
  <li>Estimation<svg width="4" height="7"><path d="M0 0l4 3.5L0 7z" fill="#555"/></svg></li>
</ul>

<!-- options panel -->
<section class="abs panel options"><div class="panel-head">Select Your options</div></section>
<div class="abs dropdown" style="left:327px;top:425px;width:136px">Filter Caterogy<svg width="8" height="5"><path d="M0 0h8L4 5z" fill="#777"/></svg></div>
<div class="abs dropdown" style="left:476px;top:425px;width:136px">Sort by<svg width="8" height="5"><path d="M0 0h8L4 5z" fill="#777"/></svg></div>

<table class="abs flashcard" style="left:319px;top:482px"><tr><td>25</td><td>25</td><td>25</td><td>25</td></tr><tr><td>65</td><td>65</td><td>65</td><td>65</td></tr></table>
<div class="abs caption" style="left:319px;top:541px;width:142px">Number Flashcards</div>
<div class="abs thumb" style="left:489px;top:477px;width:133px;height:54px;background:linear-gradient(90deg,#b5653a,#e8d9c8,#b5653a)" role="img" aria-label="Cartoon fox characters"></div>
<div class="abs caption" style="left:480px;top:541px;width:140px">Counting Pages</div>

<table class="abs flashcard" style="left:319px;top:632px"><tr><td>25</td><td>25</td><td>25</td><td>25</td></tr><tr><td>65</td><td>65</td><td>65</td><td>65</td></tr></table>
<div class="abs caption" style="left:319px;top:691px;width:142px">Number Flashcards</div>
<div class="abs thumb" style="left:489px;top:627px;width:133px;height:54px;background:linear-gradient(90deg,#b5653a,#e8d9c8,#b5653a)" role="img" aria-label="Cartoon fox characters"></div>
<div class="abs caption" style="left:480px;top:691px;width:140px">Counting Pages</div>

<div class="abs thumb" style="left:327px;top:758px;width:129px;height:34px;background:linear-gradient(90deg,#d42a2a,#e85a4a,#d42a2a)" role="img" aria-label="Red dice illustrations"></div>
<div class="abs caption" style="left:320px;top:815px;width:142px">Dice Counting</div>
<div class="abs thumb" style="left:493px;top:758px;width:129px;height:34px;background:linear-gradient(90deg,#d42a2a,#e85a4a,#d42a2a)" role="img" aria-label="Red dice illustrations"></div>
<div class="abs caption" style="left:494px;top:815px;width:142px">Dice Counting</div>

<table class="abs flashcard plain" style="left:319px;top:865px"><tr><td>25</td><td>25</td><td>25</td><td>25</td></tr><tr><td>65</td><td>65</td><td>65</td><td>65</td></tr></table>
<div class="abs caption" style="left:316px;top:924px;width:146px">Number Recognition Sheets</div>
<div class="abs thumb" style="left:499px;top:869px;width:126px;height:44px;background:linear-gradient(90deg,#3c63b0,#e89a30,#3c63b0)" role="img" aria-label="Cartoon bluebird characters"></div>
<div class="abs caption" style="left:492px;top:924px;width:140px">Counting Flashcards</div>

<!-- generator panel -->
<section class="abs panel generator"><div class="panel-head">Generate Your Worksheets</div></section>

<div class="abs field-label" style="left:650px;top:435px;width:120px;text-align:left;padding-left:61px">Nubmber of Problems :</div>
<div class="abs select" style="left:781px;top:431px"><span>Select</span><i><svg width="8" height="5"><path d="M0 0h8L4 5z" fill="#777"/></svg></i></div>

<div class="abs field-label" style="left:649px;top:485px">Format :</div>
<div class="abs select" style="left:781px;top:481px"><span>Select</span><i><svg width="8" height="5"><path d="M0 0h8L4 5z" fill="#777"/></svg></i></div>

<div class="abs field-label" style="left:652px;top:531px">Terms :</div>
<div class="abs select" style="left:781px;top:528px"><span>Select</span><i><svg width="8" height="5"><path d="M0 0h8L4 5z" fill="#777"/></svg></i></div>

<div class="abs field-label" style="left:652px;top:578px">Min :</div>
<div class="abs select" style="left:781px;top:575px"><span>Select</span><i><svg width="8" height="5"><path d="M0 0h8L4 5z" fill="#777"/></svg></i></div>

<div class="abs field-label" style="left:648px;top:629px">Max :</div>
<div class="abs select" style="left:781px;top:626px"><span>Select</span><i><svg width="8" height="5"><path d="M0 0h8L4 5z" fill="#777"/></svg></i></div>

<div class="abs field-label" style="left:648px;top:683px">Decimal Places :</div>
<div class="abs select" style="left:781px;top:680px"><span>Select</span><i><svg width="8" height="5"><path d="M0 0h8L4 5z" fill="#777"/></svg></i></div>

<div class="abs field-label" style="left:726px;top:725px;text-align:left">Express :</div>
<div class="abs radio on" style="left:734px;top:746px"><b></b>Improper Fractions</div>
<div class="abs radio" style="left:734px;top:780px"><b></b>Mixed Fractions</div>
<div class="abs radio" style="left:734px;top:808px"><b></b>Decimals</div>

<div class="abs format-icon" style="left:778px;top:852px;background:#e0433a" role="img" aria-label="PDF format option"></div>
<div class="abs format-icon" style="left:815px;top:848px;height:33px;background:#e9582a" role="img" aria-label="HTML format option"></div>

<div class="abs generate">GENERATE</div>

<!-- footer -->
<footer class="abs footer"></footer>
<div class="abs foot-links" style="left:130px;top:1132px">Home<span class="sep">|</span>About Us<span class="sep">|</span>Community<span class="sep">|</span>How it Works<span class="sep">|</span>Blog<span class="sep">|</span>Help/Support<span class="sep">|</span>Contact Us</div>
<div class="abs foot-rule"></div>
<div class="abs foot-links" style="left:131px;top:1165px">Site Map<span class="sep">|</span>Privacy Policy<span style="margin-left:23px">Sheetwright.com Copyright 2013. All rights reserved.</span></div>
<div class="abs foot-head" style="left:594px;top:1129px">SUBSCRIBE TO OUR NEWSLETTER</div>
<div class="abs newsletter">Email Address<b>SUBSCRIBE</b></div>
<div class="abs foot-head" style="left:826px;top:1129px">FOLLOW US ON</div>
<div class="abs social" style="left:838px;top:1149px;background:#3b5ea8"></div>
<div class="abs social" style="left:863px;top:1149px;background:#4fb8ea"></div>

</body>
</html>
```